Webdesign für Maklerbüro
Zielgruppe
Wir sind ein Maklerbüro aus Nürnberg, das sich auf den Verkauf von Eigentumswohnungen und Häuser spezialisiert hat. Mit der neuen Seite möchten wir vor allem Eigentümer ansprechen und über unsere Arbeitsweise informieren. Der Hauptzweck ist damit die Akquise von neuen Objekten, für die Vermittlung. Die Zielgruppe sind vornehmlich Immobilienbesitzer im Alter 40+ und im gehobenen Preissegment.
Aufgabenstellung
Beim Design bitte an den Vorgaben des Logo (Datei beigefügt) orientieren. Bilder und Texte können durch 'Platzhalter' ersetzt werden.
Grundsätzlich stellt es für uns kein Problem dar, sich an Template-Vorlagen zu orientieren. Wir stellen uns eine Seite mit Pfiff und Ideenreichtum – einfach weg vom Standard – vor. Wir verkaufen Immobilien, aber vom verstaubten Krawattenträger sind wir weit entfernt. Wir sind ein junges Unternehmen, das neue Marketingwege beschreitet. Unsere Webseite muss das ausdrücken. Kein Standard, und damit auch keine Standard-Webseite. Designs, die uns gut gefallen (und in die Richtung es auch gehen kann) haben wir beigefügt.

```html
<!DOCTYPE html>
<html lang="de">
<head>
<meta charset="utf-8">
<title>Wohnkante – Ulmenpark</title>
<link href="https://fonts.googleapis.com/css2?family=Open+Sans:wght@300;400;600;700&family=Cinzel:wght@400&display=swap" rel="stylesheet">
<style>
:root{
  --blue:#0399d8;
  --navy:#1c2344;
  --ink:#3a3a3a;
  --muted:#6b6b6b;
  --grey:#e1e1e3;
  --field:#f1f1f1;
  --white:#ffffff;
  --orange:#e9a12a;
}
*{margin:0;padding:0;box-sizing:border-box}
html,body{width:697px;height:1200px;overflow:hidden;background:var(--white)}
body{font-family:"Open Sans",Arial,sans-serif;color:var(--ink);position:relative}
.page{position:relative;width:697px;height:1200px;overflow:hidden}
.abs{position:absolute}

/* hero */
.hero{left:0;top:0;width:697px;height:372px;border-top:1px solid #1b4f8a;
  background:linear-gradient(160deg,#2f3a2c 0%,#4a5446 28%,#5d6266 50%,#4b5a41 72%,#2f3b2a 100%)}
.hero-shade{left:0;top:0;width:697px;height:372px;background:linear-gradient(180deg,rgba(0,0,0,.45) 0%,rgba(0,0,0,.05) 30%,rgba(0,0,0,0) 100%)}
.brand{left:70px;top:12px;color:var(--white);font-weight:700;font-size:11px;letter-spacing:.3px;display:flex;align-items:center;gap:4px}
.brand .mark{width:8px;height:8px;background:var(--white)}
.brand small{display:block;font-weight:400;font-size:4.2px;letter-spacing:2px;margin-top:1px}
.contact{left:0;width:697px;top:15px;text-align:center;color:var(--white);font-size:6px;line-height:10px}
.contact b{font-weight:400;font-size:7.5px}
.contact span{font-size:7.5px}
.tools{left:604px;top:19px;display:flex;gap:5px;align-items:center}
.hero-title{left:0;width:697px;top:142px;text-align:center;color:var(--white);font-family:"Cinzel",serif;font-size:17px;letter-spacing:.5px}
.hero-addr{left:0;width:697px;top:167px;text-align:center;color:var(--white);font-size:9px;font-weight:300}
.thumb{top:303px;width:60px;height:60px;border:1.5px solid rgba(255,255,255,.8)}
.t1{left:198px;background:linear-gradient(135deg,#e9e6de,#9b9586)}
.t2{left:276px;background:linear-gradient(160deg,#e8a447,#6a5230)}
.t3{left:352px;background:linear-gradient(160deg,#a3412d,#5a2119)}
.t4{left:429px;background:linear-gradient(160deg,#d6e0f0,#3b4f8e)}

/* listings */
.listing-band{left:0;top:335px;width:697px;height:136px}
.listing{top:376px;width:200px;text-align:center;color:var(--white)}
.listing h3{font-weight:300;font-size:11.5px;line-height:15px}
.listing p{font-weight:300;font-size:8px;line-height:12px}
.facts{top:421px;display:flex}
.fact{width:38px;height:34px;border:1px solid rgba(255,255,255,.6);color:var(--white);text-align:center;font-size:6.6px;font-weight:300;padding-top:4px}
.fact svg{display:block;margin:0 auto 3px}
.fact .eur{display:block;font-size:13px;font-weight:700;line-height:14px;margin-bottom:2px}

/* side share */
.chat{left:0;top:274px;width:16px;height:53px;background:var(--orange);color:var(--white);font-size:4px;font-weight:700}
.chat span{position:absolute;left:3px;top:34px;transform:rotate(-90deg);transform-origin:left top;white-space:nowrap;letter-spacing:.3px}
.chat i{position:absolute;left:4px;top:38px;width:7px;height:9px;border:1px solid var(--white)}
.share{left:0;width:16px;height:16px}
.share::after{content:"";position:absolute;left:5px;top:5px;width:6px;height:6px;background:var(--white)}

/* details */
.map{left:70px;top:499px;width:241px;height:224px;background:linear-gradient(135deg,#ede6d3 0%,#e3dcc7 45%,#a8c4e8 60%,#f0d894 75%,#ede6d3 100%)}
.details{left:329px;top:505px;width:295px}
.details h2{font-weight:300;font-size:14.5px;color:#333;margin-left:2px;margin-bottom:8px}
.details p{font-weight:300;font-size:6.5px;line-height:14px;color:var(--muted);margin-bottom:14px}

/* call to action */
.cta{left:0;top:739px;width:697px;height:49px;background:var(--blue)}
.cta-text{left:238px;top:759px;color:var(--white);font-size:8.5px;font-weight:300}
.cta-btn{left:366px;top:755px;width:94px;height:20px;background:var(--navy);border-radius:3px;color:var(--white);font-size:8.5px;font-weight:300;text-align:center;line-height:20px}

/* contact form */
.touch{left:0;top:788px;width:697px;height:267px;background:var(--grey)}
.touch h2{position:absolute;left:0;width:697px;top:35px;text-align:center;font-family:"Cinzel",serif;font-weight:400;font-size:15px;color:#222}
.touch .rule{position:absolute;left:305px;top:54px;width:59px;height:1px;background:var(--blue)}
.touch .lead{position:absolute;left:0;width:697px;top:66px;text-align:center;font-size:6.8px;font-weight:300;line-height:11px;color:#333}
.field{background:var(--field);border-radius:2px;color:#a9a9a9;font-size:6.5px;font-weight:300;padding:6px 5px}
.send{left:266px;top:963px;width:347px;height:23px;background:var(--blue);border-radius:2px;color:var(--white);font-size:7px;text-align:center;line-height:23px}
.soc{top:1021px;width:20px;height:20px;background:#f4f4f4;border:1px solid #d6d6d6}
.soc::after{content:"";position:absolute;left:7px;top:7px;width:5px;height:5px;background:#8c8c8c}

/* stats */
.stats{left:0;top:1055px;width:697px;height:36px}
.stat{color:var(--white);font-weight:300}
.stat b{font-weight:400;font-size:13px;display:block;line-height:14px}
.stat small{font-size:4.6px;display:block}

/* footer */
.fnav{left:0;width:697px;top:1094px;text-align:center;font-size:7px;color:#333}
.fnav span{margin:0 5px}
.fbrand{left:0;width:697px;top:1122px;text-align:center;color:var(--navy);font-weight:700;font-size:10px}
.fbrand i{display:inline-block;width:7px;height:7px;background:var(--navy);margin-right:3px;vertical-align:0}
.fsoc{left:316px;top:1146px;display:flex;gap:10px}
.fsoc span{width:9px;height:9px;background:var(--blue);border-radius:1px}
.fine{left:0;width:697px;text-align:center;font-size:5.8px;color:#555}
.fine a{color:var(--blue)}
</style>
</head>
<body>
<div class="page">

  <div class="abs hero" role="img" aria-label="Luftaufnahme der Wohnanlage mit Gärten und Bäumen"></div>
  <div class="abs hero-shade"></div>

  <div class="abs brand"><span class="mark"></span><div>WOHNKANTE<small>IMMOBILIENVERTRIEB</small></div></div>

  <div class="abs contact">
    <div>&#9742; Kontaktieren Sie mich direkt? <b>0911 5550 1234</b></div>
    <div><span>&#9993; kontakt@wohnkante-beispiel.de</span></div>
  </div>

  <div class="abs tools">
    <svg width="9" height="9" viewBox="0 0 10 10"><circle cx="4" cy="4" r="3" fill="none" stroke="#fff" stroke-width="1.6"/><line x1="6.2" y1="6.2" x2="9.3" y2="9.3" stroke="#fff" stroke-width="1.8"/></svg>
    <svg width="9" height="8" viewBox="0 0 9 8"><rect y="0" width="9" height="1.4" fill="#0399d8"/><rect y="3.3" width="9" height="1.4" fill="#0399d8"/><rect y="6.6" width="9" height="1.4" fill="#0399d8"/></svg>
  </div>

  <div class="abs hero-title">ULMENPARK</div>
  <div class="abs hero-addr">Lindenauer Weg 12, 90000 Musterau</div>

  <svg class="abs listing-band" viewBox="0 0 697 136" width="697" height="136">
    <polygon points="0,34 697,0 697,136 0,136" fill="#0399d8"/>
  </svg>

  <div class="abs thumb t1" role="img" aria-label="Foto Wohnzimmer"></div>
  <div class="abs thumb t2" role="img" aria-label="Foto Stadt bei Sonnenuntergang"></div>
  <div class="abs thumb t3" role="img" aria-label="Foto Backsteinfassade"></div>
  <div class="abs thumb t4" role="img" aria-label="Foto Glasfassade"></div>

  <div class="abs listing" style="left:40px"><h3>Gartenwohnung</h3><p>Neubau, EG</p></div>
  <div class="abs listing" style="left:248px"><h3>Gartenwohnung</h3><p>Neubau, EG</p></div>
  <div class="abs listing" style="left:456px"><h3>Gartenwohnung</h3><p>Neubau, EG</p></div>

  <div class="abs facts" style="left:70px">
    <div class="fact"><svg width="18" height="10" viewBox="0 0 18 10"><rect x="0" y="0" width="2" height="10" fill="#fff"/><circle cx="5" cy="3.5" r="2" fill="#fff"/><rect x="8" y="2" width="10" height="4" fill="#fff"/><rect x="0" y="6" width="18" height="2" fill="#fff"/><rect x="16" y="6" width="2" height="4" fill="#fff"/></svg>2 Zimmer</div>
    <div class="fact" style="margin-left:13px"><svg width="10" height="12" viewBox="0 0 10 12"><rect width="10" height="12" fill="#fff"/><g fill="#0399d8"><rect x="2" y="2" width="2" height="2"/><rect x="6" y="2" width="2" height="2"/><rect x="2" y="6" width="2" height="2"/><rect x="6" y="6" width="2" height="2"/></g></svg>78 m²</div>
    <div class="fact" style="margin-left:15px"><span class="eur">€</span>329.000 €</div>
  </div>
  <div class="abs facts" style="left:277px">
    <div class="fact"><svg width="18" height="10" viewBox="0 0 18 10"><rect x="0" y="0" width="2" height="10" fill="#fff"/><circle cx="5" cy="3.5" r="2" fill="#fff"/><rect x="8" y="2" width="10" height="4" fill="#fff"/><rect x="0" y="6" width="18" height="2" fill="#fff"/><rect x="16" y="6" width="2" height="4" fill="#fff"/></svg>2 Zimmer</div>
    <div class="fact" style="margin-left:13px"><svg width="10" height="12" viewBox="0 0 10 12"><rect width="10" height="12" fill="#fff"/><g fill="#0399d8"><rect x="2" y="2" width="2" height="2"/><rect x="6" y="2" width="2" height="2"/><rect x="2" y="6" width="2" height="2"/><rect x="6" y="6" width="2" height="2"/></g></svg>78 m²</div>
    <div class="fact" style="margin-left:15px"><span class="eur">€</span>329.000 €</div>
  </div>
  <div class="abs facts" style="left:485px">
    <div class="fact"><svg width="18" height="10" viewBox="0 0 18 10"><rect x="0" y="0" width="2" height="10" fill="#fff"/><circle cx="5" cy="3.5" r="2" fill="#fff"/><rect x="8" y="2" width="10" height="4" fill="#fff"/><rect x="0" y="6" width="18" height="2" fill="#fff"/><rect x="16" y="6" width="2" height="4" fill="#fff"/></svg>2 Zimmer</div>
    <div class="fact" style="margin-left:13px"><svg width="10" height="12" viewBox="0 0 10 12"><rect width="10" height="12" fill="#fff"/><g fill="#0399d8"><rect x="2" y="2" width="2" height="2"/><rect x="6" y="2" width="2" height="2"/><rect x="2" y="6" width="2" height="2"/><rect x="6" y="6" width="2" height="2"/></g></svg>78 m²</div>
    <div class="fact" style="margin-left:15px"><span class="eur">€</span>329.000 €</div>
  </div>

  <div class="abs chat"><span>CHAT NOW</span><i></i></div>
  <div class="abs share" style="top:333px;background:#3b5998"></div>
  <div class="abs share" style="top:349px;background:#3fa9e0"></div>
  <div class="abs share" style="top:365px;background:#1f76a8"></div>
  <div class="abs share" style="top:381px;background:#8a8f96"></div>

  <div class="abs map" role="img" aria-label="Stadtplan mit Lage des Objekts"></div>

  <div class="abs details">
    <h2>Details des Objekts</h2>
    <p>Lorem ipsum dolor sit amet, consectetur adipiscing elit. In congue tempus eros, quis imperdiet ante commodo sit amet. Cras suscipit malesuada libero, a viverra urna dapibus in. Sed ut felis nulla. Class aptent taciti sociosqu ad litora torquent per conubia nostra, per inceptos himenaeos. Mauris porta porttitor aliquam. Nullam efficitur metus non dui posuere, a rhoncus enim consectetur. Quisque sit amet diam ex. Vivamus vulputate mi mi, eu dapibus arcu gravida iaculis. Pellentesque venenatis eros metus, quis consequat eros eleifend id. Donec pellentesque quis odio ac hendrerit. Sed sit amet sapien sit amet nibh viverra efficitur.</p>
    <p>Sed id pretium nisi. Phasellus vehicula risus vel dui maximus bibendum. Sed ac nisi eu dui aliquam placerat. Integer sodales sapien non nisl commodo suscipit. Ut et ullamcorper urna. Donec faucibus sapien nec augue commodo blandit. Cras tincidunt urna felis, vel sodales sem dignissim et. Praesent condimentum egestas lacus eget convallis. Maecenas placerat turpis ac odio placerat eleifend. Sed ac dui fringilla, pretium velit ut, suscipit nibh.</p>
  </div>

  <div class="abs cta"></div>
  <div class="abs cta-text">Interessiert an diesem Objekt</div>
  <div class="abs cta-btn">Expose Anfordern</div>

  <section class="abs touch">
    <h2>GET IN TOUCH</h2>
    <div class="rule"></div>
    <div class="lead">Lorem ipsum dolor sit amet, consectetur adipisicing elit, sed do eiusmod tempor incididunt ut labore et dolore magna aliqua.<br>Ut enim ad minim veniam, quis nostrud exercitation ullamco laboris nisi ut aliquip.</div>
  </section>

  <div class="abs field" style="left:85px;top:903px;width:166px;height:22px">Name</div>
  <div class="abs field" style="left:85px;top:933px;width:166px;height:22px">Email</div>
  <div class="abs field" style="left:85px;top:963px;width:166px;height:22px">Subject</div>
  <div class="abs field" style="left:266px;top:903px;width:347px;height:53px;padding-top:3px">Message Texts...</div>
  <div class="abs send">Send Message</div>

  <div class="abs soc" style="left:290px"></div>
  <div class="abs soc" style="left:317px"></div>
  <div class="abs soc" style="left:344px"></div>
  <div class="abs soc" style="left:371px"></div>
  <div class="abs soc" style="left:398px"></div>

  <svg class="abs stats" viewBox="0 0 697 36" width="697" height="36">
    <rect width="697" height="36" fill="#0399d8"/>
    <polygon points="0,0 322,0 335,18 322,36 0,36" fill="#1c2344"/>
    <g fill="#fff">
      <circle cx="122" cy="13" r="4"/><circle cx="114" cy="15" r="3"/><circle cx="130" cy="15" r="3"/>
      <rect x="116" y="18" width="12" height="9" rx="3"/><rect x="109" y="19" width="8" height="7" rx="3"/><rect x="127" y="19" width="8" height="7" rx="3"/>
      <rect x="230" y="10" width="17" height="17" fill="none" stroke="#fff" stroke-width="1.6"/>
      <rect x="230" y="10" width="17" height="4"/>
    </g>
    <g fill="none" stroke="#fff" stroke-width="1.5">
      <circle cx="370" cy="18" r="7"/><polyline points="370,14 370,18 373,18"/>
      <circle cx="532" cy="18" r="7"/><polyline points="532,14 532,18 535,18"/>
    </g>
  </svg>
  <div class="abs stat" style="left:139px;top:1061px"><b>9,000</b><small>Satisfied Customers</small></div>
  <div class="abs stat" style="left:253px;top:1061px"><b>20</b><small>Years Of Experience</small></div>
  <div class="abs stat" style="left:386px;top:1060px;text-align:center"><b style="font-size:14px">Monday - Saturday</b><small style="font-size:7px;margin-top:3px">9AM - 7PM</small></div>
  <div class="abs stat" style="left:548px;top:1060px;text-align:center"><b style="font-size:14px">Sunday</b><small style="font-size:7px;margin-top:3px">Closed</small></div>

  <div class="abs fnav"><span>Home</span><span>Eigentumer</span><span>Bewertung</span><span>Beratung</span><span>Angebote</span><span>Kontakt</span></div>
  <div class="abs fbrand"><i></i>WOHNKANTE</div>
  <div class="abs fsoc"><span></span><span></span><span></span><span></span></div>
  <div class="abs fine" style="top:1160px">Need Help ? We Are Available At 0800 - 123456789 Or Email Us At <a>info@yourdomain.com</a></div>
  <div class="abs fine" style="top:1171px">© Copyrights 2018 All Rights Reserved. Powered By: <a>Larvenwerk</a></div>

</div>
</body>
</html>
```